Business Card Design

Professional solutions in (servers, security, networks, programming)

Industry/Entity Type

Business

Contact Information for Business Card

Tarek Hounayni
Internet services and network solutions
DPV - RTLK - RTLB
netcare@qo-lam.com / 05917406238
www.qo-lam.com

```html
<!DOCTYPE html>
<html lang="en">
<head>
<meta charset="utf-8">
<title>Tarek Hounayni — Business Card</title>
<link href="https://fonts.googleapis.com/css2?family=Bebas+Neue&family=Open+Sans:wght@400&display=swap" rel="stylesheet">
<style>
  :root {
    --page: #ffffff;
    --card: #434343;
    --band: #16a6c4;
    --ink: #ffffff;
    --rule: #d8d8d8;
  }
  html, body {
    margin: 0;
    padding: 0;
    width: 1200px;
    height: 1000px;
    overflow: hidden;
    background: var(--page);
  }
  .canvas {
    position: relative;
    width: 1200px;
    height: 1000px;
  }
  .card {
    position: absolute;
    left: 218px;
    top: 275px;
    width: 765px;
    height: 449px;
    background: var(--card);
    border-radius: 50px;
    overflow: hidden;
    color: var(--ink);
    font-family: "Open Sans", Arial, sans-serif;
  }
  .rule {
    position: absolute;
    height: 1px;
    background: var(--rule);
  }
  .rule--top { left: 0; top: 79px; width: 176px; }
  .rule--bottom { left: 325px; top: 360px; width: 440px; }
  .services {
    position: absolute;
    right: 28px;
    top: 65px;
    margin: 0;
    text-align: right;
    font-size: 21px;
    line-height: 33px;
    letter-spacing: 0.2px;
  }
  .name-band {
    position: absolute;
    left: 0;
    top: 182px;
    width: 765px;
    height: 86px;
    background: var(--band);
    display: flex;
    align-items: center;
    justify-content: center;
  }
  .name {
    margin: 0;
    font-family: "Bebas Neue", Impact, sans-serif;
    font-weight: 400;
    font-size: 66px;
    letter-spacing: 1.5px;
    line-height: 1;
    padding-top: 6px;
  }
  .contact {
    position: absolute;
    left: 33px;
    top: 312px;
    margin: 0;
    padding: 0;
    list-style: none;
    font-size: 21px;
    line-height: 33px;
  }
</style>
</head>
<body>
  <div class="canvas">
    <section class="card">
      <div class="rule rule--top"></div>
      <p class="services">INTERNET SERVICES AND NETWORK SOLUTIONS<br>DPV - RTLK - RTLB</p>
      <div class="name-band">
        <h1 class="name">Tarek Hounayni</h1>
      </div>
      <ul class="contact">
        <li class="contact__phone">05917406238</li>
        <li class="contact__email">netcare@qo-lam.com</li>
        <li class="contact__web">www.qo-lam.com</li>
      </ul>
      <div class="rule rule--bottom"></div>
    </section>
  </div>
</body>
</html>
```